LumaMove In-home Personal Training

I would like to have some eye-catching business card design. Opened to any ideas.

The business idea: mobile fitness - train clients at their places

Target Market(s)

General population, 20-60 years old

Industry/Entity Type

Fitness

Contact Information for Business Card

The information to include:
Name: Marta
Call or text: 306-555-0187
Website: LumaMove.ca
Please use the attached logo

Requirements
Should not have
• No orange or purple colours please

```html
<!DOCTYPE html>
<html lang="en">
<head>
<meta charset="utf-8">
<title>LumaMove Business Card</title>
<link rel="stylesheet" href="https://fonts.googleapis.com/css2?family=Exo+2:wght@300;400;600&display=swap">
<style>
  :root {
    --backdrop: #161616;
    --card: #3c3c3c;
    --card-edge: #f2f2f2;
    --ink-light: #ffffff;
    --ink-muted: #d8d8d8;
    --ink-deep: #262626;
  }
  * { margin: 0; padding: 0; box-sizing: border-box; }
  html, body {
    width: 1200px;
    height: 900px;
    overflow: hidden;
    background: var(--backdrop);
    font-family: "Exo 2", sans-serif;
  }
  .stage {
    position: relative;
    width: 1200px;
    height: 900px;
  }
  .card {
    position: absolute;
    left: 240px;
    width: 720px;
    height: 410px;
    background: var(--card);
    border-bottom: 4px solid var(--card-edge);
    border-left: 4px solid var(--card-edge);
  }
  .card--front { top: 30px; }
  .card--back { top: 462px; }

  /* Front side: large brand name */
  .front-brand {
    position: absolute;
    left: 0;
    right: 0;
    top: 140px;
    display: flex;
    flex-direction: column;
    align-items: center;
  }
  .front-brand__row {
    display: flex;
    align-items: center;
    gap: 22px;
  }
  .front-brand__dot {
    width: 70px;
    height: 70px;
    border-radius: 50%;
    border: 6px solid var(--ink-deep);
  }
  .front-brand__name {
    font-size: 72px;
    font-weight: 300;
    letter-spacing: 10px;
    color: var(--ink-deep);
  }
  .front-brand__tagline {
    margin-top: 6px;
    margin-left: 92px;
    font-size: 13px;
    font-weight: 400;
    letter-spacing: 5px;
    text-transform: uppercase;
    color: var(--ink-deep);
  }

  /* Back side: brand + contact */
  .back-layout {
    position: absolute;
    left: 44px;
    right: 40px;
    top: 160px;
    display: flex;
    align-items: center;
  }
  .back-brand {
    display: flex;
    flex-direction: column;
  }
  .back-brand__row {
    display: flex;
    align-items: center;
    gap: 12px;
  }
  .back-brand__dot {
    width: 32px;
    height: 32px;
    border-radius: 50%;
    border: 3px solid var(--ink-light);
  }
  .back-brand__name {
    font-size: 36px;
    font-weight: 300;
    letter-spacing: 6px;
    color: var(--ink-light);
  }
  .back-brand__tagline {
    margin-top: 2px;
    margin-left: 44px;
    font-size: 8px;
    letter-spacing: 3px;
    text-transform: uppercase;
    color: var(--ink-muted);
  }
  .divider {
    width: 2px;
    height: 96px;
    margin: 0 28px;
    background: var(--ink-muted);
  }
  .contact__name {
    font-size: 44px;
    font-weight: 400;
    color: var(--ink-light);
    line-height: 1.1;
    margin-bottom: 10px;
  }
  .contact__line {
    font-size: 20px;
    font-weight: 400;
    color: var(--ink-light);
    line-height: 1.3;
  }
  .contact__line strong { font-weight: 600; }
</style>
</head>
<body>
<main class="stage">
  <section class="card card--front" aria-label="Card front">
    <div class="front-brand">
      <div class="front-brand__row">
        <span class="front-brand__dot"></span>
        <span class="front-brand__name">LumaMove</span>
      </div>
      <span class="front-brand__tagline">In-home personal training</span>
    </div>
  </section>

  <section class="card card--back" aria-label="Card back">
    <div class="back-layout">
      <div class="back-brand">
        <div class="back-brand__row">
          <span class="back-brand__dot"></span>
          <span class="back-brand__name">LumaMove</span>
        </div>
        <span class="back-brand__tagline">In-home personal training</span>
      </div>
      <span class="divider"></span>
      <div class="contact">
        <p class="contact__name">Marta</p>
        <p class="contact__line">Call or text: 306-555-0187</p>
        <p class="contact__line">Website: www.<strong>LumaMove.</strong>ca</p>
      </div>
    </div>
  </section>
</main>
</body>
</html>
```